Corvane Real Estate Business Card

hello, we are a real estate company located in Los Angeles, california. we are a boutique, small company but we like a big corportate look. a simple, sleek, modern and progressive look. we would like the option of having a design that could include the real estate agents personal photo and also a design if the realtor desides not to have a photo. We also would like a hotizontal design.

Corvane Properties
3817 S Hadderly
Marlow Heights, CA 90817
www.CorvaneRE.example

Gavin Prosk
Broker
BRE # 04829176
(555) 274-6390
gavin@corvanere.example

```html
<!DOCTYPE html>
<html lang="en">
<head>
<meta charset="utf-8">
<title>Corvane Real Estate Business Card</title>
<link href="https://fonts.googleapis.com/css2?family=Arimo:wght@400;700&display=swap" rel="stylesheet">
<style>
  :root {
    --backdrop: #d9dadc;
    --card-white: #fbfbfb;
    --brand-blue: #1a4e92;
    --brand-blue-dark: #15427d;
    --text-light: #ffffff;
    --divider: rgba(255, 255, 255, 0.45);
  }
  * { margin: 0; padding: 0; box-sizing: border-box; }
  html, body {
    width: 1200px;
    height: 900px;
    overflow: hidden;
    background: var(--backdrop);
    font-family: "Arimo", Arial, sans-serif;
  }
  .business-card {
    position: absolute;
    left: 110px;
    top: 170px;
    width: 980px;
    height: 560px;
    background: var(--card-white);
    box-shadow: 0 12px 30px rgba(0, 0, 0, 0.18);
    overflow: hidden;
  }
  .brand-area {
    position: absolute;
    left: 0; top: 0;
    width: 100%;
    height: 290px;
    display: flex;
    align-items: center;
    justify-content: center;
    padding-left: 140px;
  }
  .brand-name {
    display: flex;
    align-items: center;
    gap: 18px;
    color: var(--brand-blue);
    font-weight: 700;
    font-size: 52px;
    letter-spacing: -0.5px;
    white-space: nowrap;
  }
  .brand-square {
    width: 46px;
    height: 46px;
    background: var(--brand-blue);
  }
  .contact-band {
    position: absolute;
    left: 0; bottom: 0;
    width: 100%;
    height: 270px;
    background: linear-gradient(180deg, var(--brand-blue) 0%, var(--brand-blue-dark) 100%);
    color: var(--text-light);
    display: grid;
    grid-template-columns: 320px 330px 330px;
  }
  .band-column {
    position: relative;
    font-size: 22px;
    line-height: 1.3;
    white-space: nowrap;
  }
  .band-column + .band-column::before {
    content: "";
    position: absolute;
    left: 0;
    top: 40px;
    bottom: 40px;
    width: 1px;
    background: linear-gradient(180deg, transparent, var(--divider), transparent);
  }
  .agent-details { padding: 60px 0 0 70px; }
  .agent-block { display: inline-block; }
  .agent-name { font-size: 28px; text-transform: uppercase; letter-spacing: 0.5px; }
  .agent-title { text-align: right; }
  .contact-details { text-align: center; padding-top: 95px; }
  .office-details { padding: 125px 0 0 40px; }
</style>
</head>
<body>
  <section class="business-card" aria-label="Corvane Properties business card">
    <div class="brand-area">
      <div class="brand-name"><span class="brand-square"></span>Corvane Properties</div>
    </div>
    <div class="contact-band">
      <div class="band-column agent-details">
        <div class="agent-block">
          <div class="agent-name">Gavin Prosk</div>
          <div class="agent-title">Broker</div>
        </div>
        <div class="agent-license">BRE # 04829176</div>
      </div>
      <div class="band-column contact-details">
        <div class="contact-phone">(555) 274-6390</div>
        <div class="contact-email">gavin@corvanere.example</div>
        <div class="contact-web">www.CorvaneRE.example</div>
      </div>
      <div class="band-column office-details">
        <div class="office-name">Corvane Properties</div>
        <div class="office-street">3817 S Hadderly</div>
        <div class="office-city">Marlow Heights, CA 90817</div>
      </div>
    </div>
  </section>
</body>
</html>
```